Boutique custom software development company needs new business card

Our nearly 20 year old custom software development company would like to better include the fact that we are now providing Bitcoin services. These new services are B2B include education (how to acquire and securely hold Bitcoin) and integrating Bitcoin payments into existing ecommerce sites or other existing systems. Please keep the card clean and simple. Attached is our current design and some other files. vexalon.example

Target Market(s)

businesses owners interested in long term relationship

Industry/Entity Type

Custom software development and Bitcoin

Contact Information for Business Card

Marcus Ellwood, marcus@vexalon.example, vexalon.example, (888) 555-VEXAL

Font styles to use
Other font styles liked:
• monospace

Requirements
Must have
• double-sided
Nice to have
• clean and simple
Should not have
• physical address

```html
<!DOCTYPE html>
<html lang="en">
<head>
<meta charset="utf-8">
<title>Vexalon Business Card</title>
<link rel="stylesheet" href="https://fonts.googleapis.com/css2?family=Courier+Prime:wght@400;700&family=Lato:wght@300;400;700&display=swap">
<style>
  :root {
    --backdrop: #7d6650;
    --card: #141a45;
    --brand-blue: #4176bd;
    --accent-orange: #f07d22;
    --ink-light: #e6e8ef;
  }
  * { margin: 0; padding: 0; box-sizing: border-box; }
  html, body { width: 900px; height: 1200px; overflow: hidden; }
  body { background: var(--backdrop); position: relative; }

  .card {
    position: absolute;
    left: 78px;
    width: 744px;
    height: 442px;
    border-radius: 40px;
    background: var(--card);
    box-shadow: 0 4px 10px rgba(0,0,0,0.35);
  }
  .card--front { top: 130px; }
  .card--back { top: 638px; }

  /* Front */
  .brand-square {
    position: absolute;
    left: 154px; top: 113px;
    width: 173px; height: 181px;
    background: var(--brand-blue);
  }
  .web-address {
    position: absolute;
    left: 110px; top: 302px;
    width: 261px;
    text-align: center;
    font-family: "Courier Prime", monospace;
    font-size: 20px;
    letter-spacing: 0.5px;
    color: var(--ink-light);
  }
  .divider {
    position: absolute;
    left: 366px; top: 113px;
    width: 2px; height: 217px;
    background: var(--accent-orange);
  }
  .contact {
    position: absolute;
    left: 400px; top: 126px;
    font-family: "Courier Prime", monospace;
    color: var(--ink-light);
  }
  .contact__name {
    font-size: 24px;
    font-weight: 400;
    letter-spacing: 2px;
    color: var(--accent-orange);
    text-transform: uppercase;
    line-height: 32px;
    margin-bottom: 8px;
  }
  .contact__line {
    display: flex;
    align-items: center;
    gap: 8px;
    font-size: 14.5px;
    letter-spacing: 0.5px;
    line-height: 25px;
  }
  .contact__icon { width: 16px; height: 14px; flex: none; }
  .services {
    margin-top: 27px;
    font-size: 14.5px;
    letter-spacing: 0.5px;
    line-height: 25px;
    list-style: none;
  }

  /* Back */
  .wordmark {
    position: absolute;
    left: 45px; top: 116px;
    width: 655px; height: 140px;
  }
  .wordmark text {
    font-family: "Lato", sans-serif;
    font-weight: 700;
    fill: var(--brand-blue);
  }
  .tagline {
    position: absolute;
    left: 0; top: 268px;
    width: 744px;
    text-align: center;
    font-family: "Lato", sans-serif;
    font-weight: 400;
    font-size: 42px;
    letter-spacing: -1px;
    color: var(--brand-blue);
  }
</style>
</head>
<body>
  <section class="card card--front">
    <div class="brand-square"></div>
    <div class="web-address">vexalon.example</div>
    <div class="divider"></div>
    <div class="contact">
      <div class="contact__name">Marcus Ellwood</div>
      <div class="contact__line">
        <svg class="contact__icon" viewBox="0 0 16 14" aria-hidden="true">
          <path d="M1 4 Q8 -1 15 4 L13 6 L11 4.5 L5 4.5 L3 6 Z" fill="#f07d22"/>
          <path d="M4 6 L12 6 L14 13 L2 13 Z" fill="#f07d22"/>
          <circle cx="8" cy="9.5" r="1.8" fill="#141a45"/>
        </svg>
        <span>(888) 555-VEXAL</span>
      </div>
      <div class="contact__line">
        <svg class="contact__icon" viewBox="0 0 16 14" aria-hidden="true">
          <rect x="1" y="3" width="14" height="9" fill="#f07d22"/>
          <path d="M1 3 L8 8.5 L15 3" fill="none" stroke="#141a45" stroke-width="1.4"/>
        </svg>
        <span>marcus@vexalon.example</span>
      </div>
      <ul class="services">
        <li>Custom software</li>
        <li>Bitcoin payments</li>
        <li>Bitcoin education</li>
      </ul>
    </div>
  </section>

  <section class="card card--back">
    <svg class="wordmark" viewBox="0 0 655 140" aria-label="Vexalon">
      <text x="0" y="130" font-size="170" textLength="655" lengthAdjust="spacingAndGlyphs">VEXALON</text>
    </svg>
    <div class="tagline">developer of custom applications</div>
  </section>
</body>
</html>
```